Label Design for a New Alcoholized Root Beer

Create a design for a new alcoholized root beer. This is a new product category in the USA growing very rapidly. Root Beer is a popular flavor of Cola, but recently, beer manufacturers have added alcohol to it and have created a new product that has gained traction on the market at a tremendous rate.

Root Beer is vintage product that has been around for a hundred years. Consumers of this product are mostly male between the age of 30 to 45. They purchase this product for its nostalgia and vintage look and taste.

This product will be in a standard 355 mL brown bottle.

It is 5.9% abv.

The name of the product is ''Odrell's Hard Root Beer''.

We have uploaded some pictures of traditional root beers to give you an idea of the feel we want our product to have and also, the bottle the product will be filled in.

Target Market(s)

Consumers are male 30-45, same market as craft beer consumers

Industry/Entity Type

Product

Requirements
Must have
• Design must have a vintage feel to it

```html
<!DOCTYPE html>
<html lang="en">
<head>
<meta charset="utf-8">
<title>Odrell's Hard Root Beer – Label</title>
<link href="https://fonts.googleapis.com/css2?family=Lobster&family=Josefin+Sans:wght@300&display=swap" rel="stylesheet">
<style>
  :root {
    --backdrop-light: #f6c64a;
    --backdrop-dark: #c9690d;
    --paper: #f7ecd2;
    --paper-edge: #e9d7ae;
    --brand-red: #8c1c1c;
    --band-red: #a5322c;
    --cream: #fbf3df;
    --mug-gold: #e0a928;
    --foam: #ffffff;
    --ink: #4a4036;
  }
  html, body {
    margin: 0;
    padding: 0;
    width: 857px;
    height: 1200px;
    overflow: hidden;
  }
  body {
    background: radial-gradient(circle at 40% 40%, var(--backdrop-light), var(--backdrop-dark) 80%);
  }
  .label {
    position: absolute;
    left: 78px;
    top: 300px;
    width: 700px;
    height: 600px;
    display: block;
  }
  .tagline {
    font-family: "Lobster", cursive;
    font-size: 30px;
    fill: var(--cream);
  }
  .brand-name {
    font-family: "Lobster", cursive;
    font-size: 72px;
    fill: var(--brand-red);
  }
  .strength {
    font-family: "Josefin Sans", sans-serif;
    font-weight: 300;
    font-size: 30px;
    fill: var(--ink);
  }
</style>
</head>
<body>
<svg class="label" viewBox="0 0 700 600" xmlns="http://www.w3.org/2000/svg" aria-label="Odrell's Hard Root Beer label">
  <defs>
    <radialGradient id="paperGlow" cx="50%" cy="45%" r="70%">
      <stop offset="0%" stop-color="#fffaf0"/>
      <stop offset="70%" stop-color="var(--paper)"/>
      <stop offset="100%" stop-color="var(--paper-edge)"/>
    </radialGradient>
    <linearGradient id="mugTone" x1="0" y1="0" x2="0" y2="1">
      <stop offset="0%" stop-color="var(--foam)"/>
      <stop offset="35%" stop-color="#f4e6c0"/>
      <stop offset="60%" stop-color="var(--mug-gold)"/>
      <stop offset="100%" stop-color="#c98d1a"/>
    </linearGradient>
  </defs>

  <rect class="label-paper" x="0" y="0" width="700" height="600" fill="url(#paperGlow)"/>

  <polygon class="corner-band" points="0,95 300,0 380,0 0,160" fill="var(--band-red)"/>
  <text class="tagline" x="40" y="132" transform="rotate(-18 40 132)">Always Cold!</text>

  <rect class="mug-artwork" x="215" y="40" width="270" height="290" rx="24"
        fill="url(#mugTone)" role="img"
        aria-label="Engraved golden mug with splashing foam, framed by hop sprigs"/>

  <text class="brand-name" x="350" y="420" text-anchor="middle">Odrell's Hard</text>
  <text class="brand-name" x="350" y="505" text-anchor="middle">Root Beer</text>

  <text class="strength" x="655" y="572" text-anchor="end">5.9% abv.</text>
</svg>
</body>
</html>
```